Roofing Company Now Hiring and Call Now Facebook Ads

Trying to hire new sales reps in our Alabama market to add to our growing team. This is a great opportunity for any one looking for a career change or looking to add time back to the time they get to spend at home with their families. This is a chance to build a career in one of the fastest growing industries in the country and build financial freedom and a solid future for your family while easily making 6 figures yearly. Sales reps get to set their own schedule, take vacations when they want, and could even choose if they wanted to work in the summer or the winter seasons if they dont like the heat/cold environment. Sales reps are commission based with bonus/incentives for completing task and assignments weekly.

"Let's Talk About Your Roof!" Schedule a free Roof Inspection today!

Needing facebook ads for hiring and a few ads templates for daily post regarding roof inspections and roof replacements, if they are editable it would be easier for me to manage a few templates. This project needs to have a swag/cleanish look that attracts the younger group of people but still make the older group of customer think, man these guys have some solid looking things going on and looks like a well managed and built company. We also target the upper scale areas when seeking customers.

Lets see what yall got! lets Gooo!

Target Market(s)

Property owners, sales reps, homeowners, property managers, job seekers

Industry/Entity Type

Roofing Contractor Storm Restoration Contractor, Construction Contractor

Font styles to use
Sans Serif

Colors
EB3D1F
EC4F4E
F09395
F8D3D4
FCEDEE

Requirements
Must have
• Clean modern professional look with visible red and black colors, we like white too.
Nice to have
• red, black, white, popping eye catching colors.
Should not have
• wrong color red, red is more of a kelvard herons red, please stay away from the pinkish red.

```html
<!DOCTYPE html>
<html lang="en">
<head>
<meta charset="utf-8">
<title>Ridgeline Roofing – Brand Set</title>
<link rel="stylesheet" href="https://fonts.googleapis.com/css2?family=Alfa+Slab+One&family=Montserrat:ital,wght@0,400;0,500;0,600;0,700;0,800;1,500&display=swap">
<style>
  :root {
    --navy: #1e2a5c;
    --navy-deep: #18224d;
    --royal: #2b3a94;
    --red: #eb2436;
    --grey: #b4b6ba;
    --ink: #1a1a1a;
    --paper: #ffffff;
    --canvas: #f4f5f7;
  }
  * { box-sizing: border-box; margin: 0; padding: 0; }
  html, body { width: 1200px; height: 1200px; overflow: hidden; }
  body { background: var(--paper); font-family: "Montserrat", sans-serif; color: var(--ink); position: relative; }

  /* ---------- brand wordmark ---------- */
  .wordmark { font-family: "Montserrat", sans-serif; font-weight: 800; color: var(--red); text-transform: uppercase; line-height: 1; text-align: center; }
  .wordmark span { display: block; }

  /* ---------- stationery area ---------- */
  .stationery { position: absolute; left: 0; top: 0; width: 742px; height: 484px; background: var(--canvas); }
  .card { position: absolute; width: 330px; height: 190px; background: var(--paper); box-shadow: 0 4px 14px rgba(0,0,0,.14); overflow: hidden; }
  .card--front { left: 26px; top: 150px; }
  .card--back { left: 386px; top: 150px; }

  .card--front .wordmark { position: absolute; left: 0; right: 0; top: 34px; font-size: 30px; }
  .card--front .wordmark span + span { font-size: 15px; color: var(--red); margin-top: 4px; letter-spacing: 2px; }
  .card-tagline { position: absolute; left: 20px; right: 20px; top: 112px; text-align: center; font-size: 11px; line-height: 1.5; color: #555; }
  .card-tagline em { color: var(--red); font-style: italic; font-weight: 500; }

  .card-back-art { position: absolute; inset: 0; }
  .card-name { position: absolute; left: 26px; top: 28px; }
  .card-name h3 { font-size: 13px; font-weight: 700; color: var(--ink); }
  .card-name p { font-size: 7px; color: #555; margin-top: 1px; }
  .card-name p::after { content: ""; display: block; width: 46px; height: 2px; background: var(--red); margin-top: 3px; }
  .card--back .wordmark { position: absolute; right: 16px; top: 42px; font-size: 15px; }
  .card--back .wordmark span + span { font-size: 8px; margin-top: 2px; letter-spacing: 1px; }
  .card-contacts { position: absolute; left: 20px; top: 92px; display: grid; grid-template-columns: 96px 120px; gap: 8px 10px; color: var(--paper); font-size: 7.5px; line-height: 1.35; }
  .contact-row { display: flex; gap: 5px; align-items: flex-start; white-space: nowrap; }
  .contact-row svg { flex: 0 0 auto; margin-top: 1px; }

  .logo-display { position: absolute; left: 790px; top: 170px; width: 340px; }
  .logo-display .wordmark { font-size: 58px; }
  .logo-display .wordmark span + span { font-size: 30px; margin-top: 8px; letter-spacing: 4px; }

  /* ---------- hiring ad ---------- */
  .hiring-ad { position: absolute; left: 96px; top: 548px; width: 1057px; height: 556px; background: var(--paper); box-shadow: 0 0 16px rgba(0,0,0,.12); overflow: hidden; }
  .hiring-ad__art { position: absolute; inset: 0; }
  .hiring-ad__brand { position: absolute; left: 48px; top: 58px; width: 226px; }
  .hiring-ad__brand .wordmark { font-size: 36px; }
  .hiring-ad__brand .wordmark span + span { font-size: 19px; margin-top: 6px; letter-spacing: 3px; }

  .headline { position: absolute; left: 38px; top: 188px; font-family: "Alfa Slab One", serif; font-weight: 400; line-height: 1.02; text-transform: uppercase; }
  .headline__lead { display: block; font-size: 40px; color: var(--navy); letter-spacing: -0.5px; }
  .headline__role { display: block; font-size: 82px; color: var(--red); margin-top: 6px; letter-spacing: -1px; line-height: .95; }

  .hiring-ad__copy { position: absolute; left: 45px; top: 370px; width: 450px; font-size: 17px; line-height: 1.28; color: var(--ink); }
  .hiring-ad__copy strong { font-weight: 700; }
  .hiring-ad__cta { position: absolute; left: 32px; top: 457px; font-size: 15px; font-weight: 700; color: var(--red); text-transform: uppercase; }
  .hiring-ad__contacts { position: absolute; left: 38px; top: 487px; display: flex; gap: 10px; align-items: center; font-size: 17px; line-height: 1.25; }
</style>
</head>
<body>

  <section class="stationery">
    <article class="card card--front">
      <div class="wordmark"><span>Ridgeline</span><span>Roofing</span></div>
      <p class="card-tagline"><em>"Let's Talk About Your Roof!"</em> Schedule a free Roof Inspection today!</p>
    </article>

    <article class="card card--back">
      <svg class="card-back-art" viewBox="0 0 330 190" width="330" height="190" aria-hidden="true">
        <polygon points="50,0 150,0 140,16 40,16" fill="var(--red)"/>
        <polygon points="0,72 252,72 292,190 0,190" fill="var(--navy)"/>
        <polygon points="306,132 330,120 330,190 300,190" fill="var(--navy)"/>
      </svg>
      <div class="card-name">
        <h3>Dario Fenwick</h3>
        <p>Marketing Manager</p>
      </div>
      <div class="wordmark"><span>Ridgeline</span><span>Roofing</span></div>
      <div class="card-contacts">
        <div class="contact-row">
          <svg width="9" height="9" viewBox="0 0 10 10"><circle cx="5" cy="5" r="5" fill="var(--red)"/><path d="M3.3 2.6l1 1-.5.7c.4.8.9 1.3 1.6 1.6l.7-.5 1 1-.6.9c-1.9-.3-3.2-1.6-3.6-3.6z" fill="#fff"/></svg>
          <div>+555-014-2290<br>+555-014-2291</div>
        </div>
        <div class="contact-row">
          <svg width="9" height="9" viewBox="0 0 10 10"><circle cx="5" cy="5" r="5" fill="var(--red)"/><circle cx="5" cy="5" r="2.6" fill="none" stroke="#fff" stroke-width=".8"/><path d="M2.4 5h5.2M5 2.4v5.2" stroke="#fff" stroke-width=".6"/></svg>
          <div>www.summitpeakroof.com<br>hello@summitpeakroof.com</div>
        </div>
        <div class="contact-row">
          <svg width="9" height="9" viewBox="0 0 10 10"><circle cx="5" cy="5" r="5" fill="var(--red)"/><path d="M5 2.2a1.8 1.8 0 0 1 1.8 1.8c0 1.3-1.8 3.6-1.8 3.6S3.2 5.3 3.2 4A1.8 1.8 0 0 1 5 2.2z" fill="#fff"/></svg>
          <div>48 Harbor Lane,<br>Millbrook, ST 40211</div>
        </div>
      </div>
    </article>
  </section>

  <div class="logo-display">
    <div class="wordmark"><span>Ridgeline</span><span>Roofing</span></div>
  </div>

  <section class="hiring-ad">
    <svg class="hiring-ad__art" viewBox="0 0 1057 556" width="1057" height="556">
      <defs>
        <linearGradient id="crewPhotoTone" x1="0" y1="0" x2="1" y2="1">
          <stop offset="0" stop-color="#3a4a7e"/>
          <stop offset=".55" stop-color="#26366b"/>
          <stop offset="1" stop-color="#1c2857"/>
        </linearGradient>
      </defs>
      <polygon points="716,0 1057,0 1057,556 565,556 490,430" fill="url(#crewPhotoTone)" role="img" aria-label="Photo of a roofer in a hard hat at work, with a smiling businessman and businesswoman standing arms crossed in front"/>
      <polygon points="643,59 720,59 630,226 555,226" fill="var(--royal)"/>
      <polygon points="683,145 739,145 640,312 575,312" fill="var(--red)"/>
    </svg>

    <div class="hiring-ad__brand">
      <div class="wordmark"><span>Ridgeline</span><span>Roofing</span></div>
    </div>

    <h1 class="headline">
      <span class="headline__lead">We are looking<br>for a new</span>
      <span class="headline__role">Sale Rep.</span>
    </h1>

    <p class="hiring-ad__copy">We are looking for candidates who would build a long-term career with us. <strong>Are you the one?</strong></p>

    <p class="hiring-ad__cta">Send you resume to:</p>
    <div class="hiring-ad__contacts">
      <svg width="20" height="20" viewBox="0 0 20 20" aria-hidden="true"><circle cx="10" cy="10" r="10" fill="var(--red)"/><circle cx="10" cy="10" r="5.5" fill="none" stroke="#fff" stroke-width="1.2"/><ellipse cx="10" cy="10" rx="2.4" ry="5.5" fill="none" stroke="#fff" stroke-width="1"/><path d="M4.5 10h11" stroke="#fff" stroke-width="1"/></svg>
      <div>www.summitpeakroof.com<br>hello@summitpeakroof.com</div>
    </div>
  </section>

</body>
</html>
```